Design Creative Banner or Gif Ads. 3 Designs To Be Selected

Come up with some creative banner ads for stonewell.co.nz

*At least 3 different winning banners will be chosen*

Please provide banner ads / gif ads in common google ads / website banner formats.

They can be gif or static but must stand out while still maintaining clear clean text and visuals, with a premium professional feel (please avoid clip art or anything that gives a cheap message).

Please keep in mind that these will likely be small ads so text needs to be large and if there's there a lot of text then use multiple frames/ pages as submit as a gif.

Style
Minimal & clean lines
Architectural or realistic images
Avoid cartoon styles, clipart, or anything that looks cheap

Font
Nexa or Montserrat or similar

Tone
Premium, serious, trustworthy — fits new builds

Colours
Option 1: Deep Navy (trust & quality) & lighter blues and warm grey
Option 2: Open to bright colours to help the ads stand out, such as (but not limited to) bright pink with black, yellow, fluorescent green, provided the messaging is still done professionally.
Our logo is attached (Stone Well Logo)

Display Sizes
Ad specs for file sizes should be file formats like JPEG, GIF, and PNG, with animations limited to a max of 30 seconds or less.
We will need several different ad sizes provided for each of the 3 selected winning designs.

• Medium Rectangle: 300 × 250 pixels
• Leaderboard: 728 × 90 pixels
• Desktop Banner ad image: (640x360 pixels)
• Desktop Banner ad image 2: (300x600 pixels)
• Possibly one or two other sizes

Flexibility to be creative
The ad text, words, upper/lower case, layout, colour, theme, and images can be adjusted to how you think it will look best. The follow example ads are just examples of what we are after but we are keen to see what you can create.

Recommendations at this point:
1. Avoid text heavy
2. Looking for more Gif ads
3. Imaging: if possible use real stock photo's rather than AI

Themes:

1
Building Soon? Start Here
Free Build Planning Pack:
✓ Build Cost Calculator
✓ Hidden Cost Checklist
✓ Builder Comparison Guide
Build With Confidence
Download Free

2
Before You Choose A Builder
Compare Price, Scope, Risk & Value
Avoid Costly Mistakes
Choose The Right Builder With Confidence
Download The Free Guide

3
Planning A New Build?
Avoid These Common Mistakes:
✗ Hidden Exclusions
✗ Missing Scope
✗ Unrealistic Allowances
✗ Budget Blowouts
Download The Free Guide

4
Before You Buy Land
Know what it could cost to build.
Avoid Costly Building Mistakes
Download Our Free Guides

5
Know Your Build Budget?
• Free Build Cost Calculator
• Hidden Cost Checklist
• Build Planning Tools
Calculate Costs (Download)

Target Market(s)

Landowners looking to build

Industry/Entity Type

Building

Font styles to use
Other font styles liked:
• Nexa or Montserrat or similar

Requirements
Should not have
• Avoid cartoon styles, clipart, or anything that looks cheap

```html
<!DOCTYPE html>
<html lang="en">
<head>
<meta charset="utf-8">
<title>Stone Well – Free Build Planning Pack</title>
<link rel="stylesheet" href="https://fonts.googleapis.com/css2?family=Arimo:wght@400;700&display=swap">
<style>
  :root {
    --bg-edge: #1a5a93;
    --bg-mid: #2476b0;
    --bg-glow: #35a6c9;
    --white: #ffffff;
    --ink: #17222f;
    --navy: #15314f;
    --tag-blue: #3b80c6;
    --green: #7cc241;
    --green-deep: #6cb433;
    --green-light: #b6e07f;
  }
  * { box-sizing: border-box; margin: 0; padding: 0; }
  html, body { width: 1200px; height: 997px; overflow: hidden; background: var(--bg-edge); }
  .banner {
    position: relative;
    width: 1200px;
    height: 997px;
    overflow: hidden;
    font-family: "Arimo", Arial, sans-serif;
    background: radial-gradient(ellipse 62% 58% at 50% 46%, var(--bg-glow) 0%, var(--bg-mid) 55%, var(--bg-edge) 100%);
  }
  .light-streak { position: absolute; left: 0; top: 0; }
  .brand-tab {
    position: absolute;
    left: 254px;
    top: -40px;
    width: 752px;
    height: 100px;
    background: var(--white);
    border-radius: 0 0 44px 44px;
  }
  .brand-row {
    position: absolute;
    left: 40px;
    right: 40px;
    top: 44px;
    display: flex;
    align-items: center;
    gap: 18px;
    white-space: nowrap;
  }
  .brand-mark {
    flex: none;
    width: 18px;
    height: 18px;
    background: var(--navy);
  }
  .brand-name {
    flex: none;
    font-size: 21px;
    font-weight: 700;
    color: var(--navy);
    line-height: 1;
    margin-right: 28px;
  }
  .brand-tagline {
    flex: none;
    font-size: 19px;
    font-weight: 700;
    letter-spacing: 0.2px;
    color: var(--tag-blue);
    text-transform: uppercase;
    line-height: 1;
  }
  .headline {
    position: absolute;
    top: 276px;
    width: 100%;
    text-align: center;
    color: var(--white);
    font-size: 64px;
    font-weight: 700;
    line-height: 1;
  }
  .subhead {
    position: absolute;
    top: 398px;
    width: 100%;
    text-align: center;
    color: var(--ink);
    font-size: 51px;
    font-weight: 700;
    line-height: 1;
  }
  .benefits {
    position: absolute;
    left: 252px;
    top: 502px;
    list-style: none;
  }
  .benefits li {
    position: relative;
    padding-left: 66px;
    color: var(--white);
    font-size: 43px;
    line-height: 60px;
  }
  .benefits li::before {
    content: "";
    position: absolute;
    left: 0;
    top: 17px;
    width: 28px;
    height: 28px;
    border-radius: 50%;
    background: var(--green);
  }
  .cta {
    position: absolute;
    top: 742px;
    height: 94px;
    border-radius: 47px;
    display: flex;
    align-items: center;
    justify-content: center;
    color: var(--ink);
    font-size: 43px;
    line-height: 1;
    white-space: nowrap;
  }
  .cta-confidence {
    left: 64px;
    width: 532px;
    background: linear-gradient(90deg, var(--green-deep) 0%, var(--green) 70%, var(--green-light) 71%, var(--green-light) 100%);
  }
  .cta-download {
    left: 610px;
    width: 530px;
    background: var(--green-light);
  }
  .site-address {
    position: absolute;
    top: 896px;
    width: 100%;
    text-align: center;
    color: var(--white);
    font-size: 46px;
    line-height: 1;
  }
</style>
</head>
<body>
  <main class="banner">
    <svg class="light-streak" width="200" height="120" viewBox="0 0 200 120" aria-hidden="true">
      <defs>
        <linearGradient id="streak" x1="0" y1="1" x2="1" y2="0">
          <stop offset="0" stop-color="#ffffff" stop-opacity="0"/>
          <stop offset="0.6" stop-color="#ffffff" stop-opacity="0.9"/>
          <stop offset="1" stop-color="#ffffff" stop-opacity="0.2"/>
        </linearGradient>
      </defs>
      <line x1="0" y1="96" x2="170" y2="0" stroke="url(#streak)" stroke-width="3"/>
    </svg>

    <header class="brand-tab">
      <div class="brand-row">
        <span class="brand-mark"></span>
        <span class="brand-name">Stone Well</span>
        <span class="brand-tagline">Compare quotes from trusted builders</span>
      </div>
    </header>

    <h1 class="headline">Building Soon? Start Here</h1>
    <h2 class="subhead">Free Build Planning Pack</h2>

    <ul class="benefits">
      <li>Build Cost Calculator</li>
      <li>Hidden Cost Checklist</li>
      <li>Builder Comparison Guide</li>
    </ul>

    <div class="cta cta-confidence">Build With Confidence</div>
    <div class="cta cta-download">Download Free</div>

    <p class="site-address">StoneWell.co.nz</p>
  </main>
</body>
</html>
```